Brindle Financial Advice - Employer Benefit Brochure

We need to design a professional looking brochure that we can present to our existing client base, and assist in attracting new clients.
The current information is just provided in a word document, but we need to improve significantly.
The audience would be business leaders, HR decision makers and member policy committee members

Industry/Entity Type

Business

Font styles to use
Sans Serif

Colors
0255a3
f37122

```html
<!DOCTYPE html>
<html lang="en">
<head>
<meta charset="utf-8">
<title>Employer Benefits Partnership – Brindle Financial Advice</title>
<link href="https://fonts.googleapis.com/css2?family=Arimo:ital,wght@0,400;0,700;1,700&display=swap" rel="stylesheet">
<style>
  :root {
    --brand-blue: #0255a3;
    --deep-blue: #08378a;
    --mid-blue: #1c62b5;
    --brand-orange: #f37122;
    --light-orange: #f7944c;
    --ink: #111111;
    --white: #ffffff;
  }
  * { margin: 0; padding: 0; box-sizing: border-box; }
  html, body { width: 927px; height: 1200px; overflow: hidden; background: var(--white); }
  body { font-family: "Arimo", Arial, sans-serif; }

  .brochure { position: relative; width: 927px; height: 1200px; overflow: hidden; }

  .masthead {
    position: absolute; top: 0; left: 0; width: 927px; height: 93px;
    background: linear-gradient(90deg, var(--deep-blue) 0%, #0e4a9e 45%, var(--mid-blue) 75%, #0b43a0 100%);
  }
  .masthead-title {
    position: absolute; left: 41px; top: 27px;
    color: var(--white); font-size: 28px; font-weight: 700; letter-spacing: -0.2px;
  }
  .masthead-divider {
    position: absolute; left: 497px; top: 21px; width: 2px; height: 47px;
    background: var(--brand-orange);
  }
  .masthead-company {
    position: absolute; left: 511px; top: 28px;
    color: var(--brand-orange); font-size: 26px; font-weight: 700; font-style: italic;
  }

  .accent-band {
    position: absolute; top: 93px; left: 0; width: 927px; height: 47px;
    background: linear-gradient(90deg, var(--brand-orange) 0%, var(--light-orange) 45%, #f3883e 70%, #e06a22 100%);
  }

  .intro { position: absolute; top: 152px; left: 42px; width: 860px; color: var(--ink); }
  .intro-heading { font-size: 22px; font-weight: 700; margin-bottom: 18px; }
  .intro-heading .tag { color: var(--brand-orange); margin-right: 6px; }
  .intro p { font-size: 17.5px; line-height: 24.5px; margin-bottom: 25px; }
  .intro .lead-in { color: var(--brand-orange); font-weight: 700; font-size: 17px; margin-top: -4px; }

  .services {
    position: absolute; top: 625px; left: 0; width: 927px; height: 575px;
    background: radial-gradient(ellipse 70% 90% at 55% 45%, #1f66b9 0%, #0f4aa0 55%, var(--deep-blue) 100%);
  }
  .service { position: absolute; left: 0; width: 927px; }
  .service-name {
    position: absolute; left: 45px; width: 340px;
    color: var(--brand-orange); font-size: 17.5px; font-weight: 700; line-height: 26px;
  }
  .service-detail {
    position: absolute; left: 400px; width: 470px;
    color: var(--white); font-size: 15.8px; line-height: 22px;
  }
</style>
</head>
<body>
<main class="brochure">
  <header class="masthead">
    <h1 class="masthead-title">Employer Benefits Partnership</h1>
    <span class="masthead-divider"></span>
    <span class="masthead-company">Company Name</span>
  </header>
  <div class="accent-band"></div>

  <section class="intro">
    <h2 class="intro-heading"><span class="tag">CORE:</span> Corporate Superannuation Services</h2>
    <p>Brindle’s core offer is the ongoing support of the group employer superannuation solution.</p>
    <p>Superannuation is a long-term investment so it’s crucial to have the right partner who will consistently deliver outstanding support to you and your employees. Brindle has an extensive knowledge of superannuation providers in the market and can ensure that you have the right solution for your long-term business requirements.</p>
    <p>We are able to take over the servicing of the current group plan, or assist in setting up a plan for companies new to the market.</p>
    <p>The program we deliver has two unique components. Firstly, services to assist employers in providing a ‘best of breed’ superannuation solution to employees and secondly, proactive advice to employees to ensure that they take control of their individual financial situation.</p>
    <p class="lead-in">Below is an overview of the services and support Brindle provides to employers:</p>
  </section>

  <section class="services">
    <div class="service" style="top:27px">
      <h3 class="service-name">Choosing your employer super plan</h3>
      <p class="service-detail" style="top:3px">Whether you are self-directed, or seeking a full advice service, we can assist you in your selection of the most suitable provider for your employees long-term retirement needs.</p>
    </div>
    <div class="service" style="top:139px">
      <h3 class="service-name">Setting up a new super plan</h3>
      <p class="service-detail" style="top:3px">We facilitate the complete application process, induction presentations for employees, lost super searches and the setting up of the online clearing facility for all your superannuation payments.</p>
    </div>
    <div class="service" style="top:245px">
      <h3 class="service-name">Managing and Reviewing your<br>employer super plan</h3>
      <p class="service-detail" style="top:1px;left:398px">We work together to build and deliver your annual Client Service Plan. We manage the annual review process, provide access to all relevant information and answer all employer and employee queries, complaints and facilitate the ongoing plan administration.</p>
    </div>
    <div class="service" style="top:373px">
      <h3 class="service-name">Policy Committee management</h3>
      <p class="service-detail" style="top:2px;left:403px">We establish and manage a Policy Committee where required or desired. Responsibilities include initiating all meetings, preparing reports, minutes and the presentation of legislative product and education updates.</p>
    </div>
    <div class="service" style="top:485px">
      <h3 class="service-name" style="left:43px">Keeping you up to date</h3>
      <p class="service-detail" style="top:2px">We provide you with all relevant communications to ensure that you meet your responsibilities and obligations.</p>
    </div>
  </section>
</main>
</body>
</html>
```